Statistical Data Science Lab website landing graphic

My lab (http://research.brindlecove.org/okafor) develops novel statistical and computational tools for analyzing and making sense of complex genomic data. I am looking for a graphic to replace the boring/generic image that is on the landing page of my website. I want something that has the words "Okafor Group" in the center with images (possibly translucent) in the background that reflect the projects that we work on in terms of using complex math and computation to analyze data from genomics and the human microbiome (bacteria in poop) studies of various diseases. The colors should mesh with the remainder of the website.

```html
<!DOCTYPE html>
<html lang="en">
<head>
<meta charset="utf-8">
<title>Okafor Group – Home</title>
<link rel="stylesheet" href="https://fonts.googleapis.com/css2?family=Arimo:ital,wght@0,400;0,600;0,700;1,400;1,700&family=Oswald:wght@500;600&display=swap">
<style>
  :root {
    --navy: #1b2d5c;
    --ink: #111111;
    --page: #ffffff;
    --backdrop: #f3f3f3;
    --cell-blue: #1f4b8c;
    --cell-blue-light: #3a6fb3;
    --purple: #a94fc9;
    --cyan: #14c1d6;
    --yellow: #fbb514;
    --muted: #8a94ad;
  }
  * { box-sizing: border-box; margin: 0; padding: 0; }
  html, body {
    width: 1200px; height: 900px; overflow: hidden;
    background: var(--backdrop);
  }
  .site {
    position: relative;
    width: 1200px; height: 900px;
    background: var(--page);
    font-family: "Arimo", Arial, sans-serif;
    color: var(--ink);
    overflow: hidden;
  }
  .site-header {
    position: absolute; top: 0; left: 0; right: 0; height: 96px;
    display: flex; align-items: center;
    padding: 0 56px;
  }
  .brand-name {
    font-family: "Oswald", "Arial Narrow", sans-serif;
    font-weight: 600; font-size: 30px; letter-spacing: 0.5px;
    color: var(--navy); text-transform: uppercase;
  }
  .main-nav {
    display: flex; gap: 46px; margin-left: 110px;
  }
  .main-nav a {
    font-size: 13px; font-style: italic; color: var(--navy);
    text-decoration: none;
  }
  .search-field {
    margin-left: auto;
    display: flex; align-items: center; gap: 8px;
    width: 200px; height: 26px;
    border: 1.5px solid var(--navy); border-radius: 13px;
    padding: 0 10px;
  }
  .search-field span {
    font-size: 12px; font-style: italic; color: var(--muted);
    border-left: 1.5px solid var(--navy); padding-left: 7px;
  }
  .hero-stripes {
    position: absolute; left: 330px; top: 110px;
    width: 300px; height: 560px;
    background: linear-gradient(150deg, var(--yellow) 0%, var(--purple) 30%, var(--navy) 55%, var(--cyan) 80%, var(--purple) 100%);
    opacity: 0.35;
    clip-path: polygon(60% 0, 100% 0, 40% 100%, 0 100%);
  }
  .hero-visual {
    position: absolute; left: -40px; top: 200px;
    width: 600px; height: 600px; border-radius: 50%;
    background: radial-gradient(circle at 40% 35%, var(--cell-blue-light) 0%, var(--cell-blue) 55%, #173a72 100%);
  }
  .hero-title {
    position: absolute; left: 20px; top: 440px; width: 480px;
    text-align: center;
    font-family: "Oswald", "Arial Narrow", sans-serif;
    font-weight: 500; font-size: 78px; line-height: 1;
    color: #ffffff; text-transform: uppercase;
  }
  .intro {
    position: absolute; left: 640px; top: 160px; width: 500px;
    text-align: center;
  }
  .intro h1 {
    font-size: 25px; font-weight: 700; font-style: italic;
    margin-bottom: 18px;
  }
  .intro p {
    font-size: 14px; line-height: 1.42; margin-bottom: 22px;
  }
  .intro strong { font-weight: 700; font-style: italic; }
  .actions {
    display: flex; justify-content: center; gap: 18px; margin-top: 30px;
  }
  .btn {
    display: inline-flex; align-items: center; justify-content: center;
    width: 92px; height: 34px; border-radius: 9px;
    font-family: "Oswald", "Arial Narrow", sans-serif;
    font-size: 13px; font-weight: 500; text-transform: uppercase;
    text-decoration: none; border: 2px solid var(--navy);
  }
  .btn-donate { background: var(--navy); color: #fff; }
  .btn-fundraise { background: #fff; color: var(--navy); }
  .affiliation {
    position: absolute; left: 700px; top: 740px; width: 380px;
    display: flex; align-items: center; justify-content: center; gap: 14px;
  }
  .affiliation-mark {
    width: 44px; height: 44px; border-radius: 50%; background: var(--navy);
  }
  .affiliation-name {
    font-size: 30px; font-weight: 600; color: var(--navy); line-height: 1.05;
  }
</style>
</head>
<body>
<div class="site">
  <header class="site-header">
    <div class="brand-name">Okafor's Group</div>
    <nav class="main-nav">
      <a href="#">Adaeze N. Okafor, P.I.</a>
      <a href="#">Group Members</a>
      <a href="#">Research</a>
      <a href="#">Software</a>
      <a href="#">Publications</a>
    </nav>
    <div class="search-field">
      <svg width="12" height="12" viewBox="0 0 12 12" aria-hidden="true">
        <circle cx="5" cy="5" r="3.6" fill="none" stroke="#1b2d5c" stroke-width="1.6"/>
        <line x1="7.7" y1="7.7" x2="11" y2="11" stroke="#1b2d5c" stroke-width="1.6" stroke-linecap="round"/>
      </svg>
      <span>e.g. Leukemia</span>
    </div>
  </header>

  <div class="hero-stripes" role="img" aria-label="Diagonal rounded stripes in purple, cyan, yellow and navy"></div>
  <div class="hero-visual" role="img" aria-label="Translucent blue microscope image of rod-shaped gut bacteria"></div>
  <div class="hero-title">Okafor Group</div>

  <section class="intro">
    <h1>Welcome to our group homepage!</h1>
    <p><strong>Adaeze Okafor</strong> is a Professor in the Biostatistics Program, Public Health Sciences Division, Brindle Cove Research Center. The major thrust of the group's research lies in the development and application of statistical methods for for analysis of high-dimensional genomic data within the broader context of clinical trials as well as population-based genetic, genomic, epigenetic, and microbiome studies. Currently, the group is heavily invested in developing and applying cutting edge approaches for microbiome and metagenomic studies. Applications focus a range of additional conditions, disorders, disease and contexts include aging, autoimmune disorders, cancer, cardiovascular disease, environmental health, and reproductive/perinatal outcomes.</p>
    <p>We are always eager to develop new collaborations with investigators within substantive fields as well as methodological researchers.</p>
    <div class="actions">
      <a class="btn btn-donate" href="#">Donate</a>
      <a class="btn btn-fundraise" href="#">Fundraise</a>
    </div>
  </section>

  <div class="affiliation">
    <div class="affiliation-mark"></div>
    <div class="affiliation-name">Brindle Cove<br>Cancer Center</div>
  </div>
</div>
</body>
</html>
```